Personal Finance Author needs a postcard

Hi there,

I am a Canadian personal finance author and have published a new book called The Wealth Compass.

I teach Millennials how to create a 6-figure portfolio through investing (https://www.dariafelt.com/)

I'm speaking at some conferences so we were going to print some postcards to hand out to attendees with our info and calls-to-action on them.

I am looking for 4x6 (horizontal) postcard (no space needed for shipping label).

Logos, Headshots and Book Cover:
https://files.cloudvaultex.com/folders/8kQpZrT2mWvN4xLbJ7sHdYc3FgA9eUoRi?usp=sharing

Both sides will be full colour. I would like a clean and simple look. Our main sites are www.DariaFelt.com and www.TheWealthCompassBook.com if you want to get a sense of style and design.
I also uploaded a few marketing materials so you can see the existing designs.

Side 1:
Get Instant Access to your Free Resources - main headline

(small bullets underneath)
- The Wealth Compass Checklist
- Financial Worksheets
- Database of Investment Tools

DariaFelt.com/Resources

At the bottom, include "Don't forget to follow Daria Felt on social media:
Linkedin: @dariafelt7
Facebook: @thewealthcompassbook Instagram: @thewealthcompassbook Twitter: @WealthCompassBk"

Side 2:
Headline - Want to work directly with Daria and The Wealth Compass team to help you make your money grow and stay safe?

Work with us to (bullet point list)...
- Hire Daria as a Keynote Speaker
- Teach Financial Literacy Workshops
- Receive Financial Coaching

Want To Learn More About How We Can Help?
DariaFelt.com/Services

Include my contact info:
Daria Felt
Author | Speaker | Investor
daria@thewealthcompassbook.com
416-555-0187

Target Market(s)

Millennials who want to learn how to save and invest their money. I focus on stock market investing, real estate investing and entrepreneurship.

Industry/Entity Type

Financial Service

Font styles to use
Sans Serif

Colors

Designer to choose colors to be used in the design.

Requirements
Must have
• Photo of Daria Felt
• The Wealth Compass logo
• Green, Gold/Yellow to match existing colours
• modern business style postcard

```html
<!DOCTYPE html>
<html lang="en">
<head>
<meta charset="utf-8">
<title>The Wealth Compass Postcard</title>
<link rel="stylesheet" href="https://fonts.googleapis.com/css2?family=Saira:ital,wght@0,700;1,700;1,800&family=Saira+Condensed:wght@700&family=Roboto:wght@400;500;700&display=swap">
<style>
  :root {
    --green: #135f34;
    --gold: #e9aa2b;
    --navy: #14202e;
    --cream: #ece8dd;
    --paper: #f5f6f8;
    --grey: #555a5f;
    --ink: #1d1d1d;
    --white: #ffffff;
  }
  * { margin: 0; padding: 0; box-sizing: border-box; }
  html, body { width: 872px; height: 1200px; overflow: hidden; background: var(--white); }
  body { position: relative; font-family: "Roboto", sans-serif; }
  .card { position: absolute; left: 0; width: 872px; border: 1.5px solid #111; overflow: hidden; }
  .card-front { top: 0; height: 580px; background: var(--cream); }
  .card-back { top: 619px; height: 581px; background: var(--paper); }
  .abs { position: absolute; }

  /* front */
  .front-shapes { position: absolute; left: 0; top: 0; width: 869px; height: 580px; }
  .headline {
    left: 22px; top: 46px; width: 390px; text-align: center;
    font-family: "Saira", sans-serif; font-style: italic; font-weight: 800;
    font-size: 47px; line-height: 55px; color: var(--navy);
    text-shadow: 0 0 8px rgba(255,255,255,.9);
  }
  .headline .accent { color: var(--green); }
  .phone-box {
    left: 54px; top: 233px; width: 306px; height: 56px; background: var(--green);
    color: var(--white); font-weight: 500; font-size: 26px; line-height: 56px; text-align: center;
    box-shadow: 0 10px 10px -6px rgba(0,0,0,.35);
  }
  .photo { background: linear-gradient(160deg, #e9dccd 0%, #b98d6c 35%, #1d2230 70%, #151821 100%); }
  .photo-front { left: 413px; top: 34px; width: 398px; height: 268px; border-radius: 160px 160px 0 0; }
  .services-title {
    left: 93px; top: 410px; font-family: "Saira Condensed", sans-serif; font-weight: 700;
    font-size: 27px; color: var(--green);
  }
  .services-list {
    left: 70px; top: 440px; list-style: none;
    font-family: "Saira", sans-serif; font-style: italic; font-weight: 700;
    font-size: 18px; line-height: 31px; color: var(--navy);
  }
  .divider { left: 372px; top: 412px; width: 5px; height: 122px; background: var(--green); }
  .visit {
    left: 416px; top: 358px; font-family: "Saira", sans-serif; font-style: italic; font-weight: 700;
    font-size: 18px; letter-spacing: .6px; color: var(--navy);
  }
  .follow {
    left: 419px; top: 392px; width: 330px; font-family: "Saira", sans-serif; font-style: italic; font-weight: 700;
    font-size: 23px; line-height: 29px; color: var(--gold);
  }
  .social { left: 420px; top: 453px; font-size: 16px; line-height: 21px; color: var(--grey); }

  .brand {
    display: flex; align-items: center; gap: 6px;
    font-family: "Roboto", sans-serif; font-weight: 700; font-size: 13px;
    color: var(--green); white-space: nowrap;
  }
  .brand-mark { width: 10px; height: 10px; background: var(--green); flex: none; }
  .brand-front { left: 712px; top: 540px; }

  /* back */
  .back-headline {
    left: 32px; top: 39px; font-family: "Saira", sans-serif; font-style: italic; font-weight: 700;
    font-size: 26.5px; line-height: 32px; color: var(--green);
  }
  .back-headline .accent { color: var(--gold); }
  .brand-back {
    left: 706px; top: 14px; height: 34px; padding: 0 10px; background: var(--white);
  }
  .photo-back { left: 509px; top: 60px; width: 307px; height: 492px; border-radius: 150px 150px 0 0; }
  .work-box { left: 0; top: 200px; width: 450px; height: 147px; background: var(--green); color: var(--white); }
  .work-title { position: absolute; left: 33px; top: 8px; font-weight: 700; font-size: 28px; }
  .work-list { position: absolute; left: 29px; top: 45px; list-style: none; font-size: 19.5px; line-height: 31px; }
  .learn-box { left: 0; top: 346px; width: 450px; height: 87px; background: var(--gold); color: var(--white);
    font-family: "Saira", sans-serif; font-style: italic; font-weight: 700; }
  .learn-q { position: absolute; left: 35px; top: 12px; font-size: 17px; }
  .learn-url { position: absolute; left: 35px; top: 42px; font-size: 23px; }
  .contact { left: 36px; top: 448px; font-size: 17.5px; line-height: 22.5px; color: var(--ink); font-style: normal; }
  .contact .tel { color: var(--green); }
  .footer-band { left: 0; bottom: 0; width: 100%; height: 29px; background: var(--green); }
</style>
</head>
<body>
  <section class="card card-front">
    <div class="abs photo photo-front" role="img" aria-label="Photo of Daria Felt smiling, holding a calculator and pointing at it"></div>
    <svg class="front-shapes" viewBox="0 0 869 580" aria-hidden="true">
      <polygon points="0,408 557,280 572,317 670,302 869,403 869,437" fill="var(--green)"/>
      <polygon points="0,408 670,302 869,437 869,580 0,580" fill="var(--white)"/>
    </svg>
    <h1 class="abs headline">Get Instant<br><span class="accent">Access</span> to your<br>Free Resources</h1>
    <div class="abs phone-box">Phone: 416-555-0187</div>
    <div class="abs visit">Visit DariaFelt.com/Resources</div>
    <h2 class="abs services-title">Services</h2>
    <ul class="abs services-list">
      <li>&nbsp;- The Wealth Compass Checklist</li>
      <li>- Financial Worksheets</li>
      <li>- Database of Investment Tools</li>
    </ul>
    <div class="abs divider"></div>
    <p class="abs follow">Don't forget to follow Daria Felt on social media:</p>
    <p class="abs social">Linkedin: @dariafelt7<br>Facebook: @thewealthcompassbook<br>Instagram: @thewealthcompassbook<br>Twitter: @WealthCompassBk</p>
    <div class="abs brand brand-front"><span class="brand-mark"></span>The Wealth Compass</div>
  </section>

  <section class="card card-back">
    <h2 class="abs back-headline">Want to work directly with<br><span class="accent">Daria and The Wealth Compass</span><br>Team to help you make your<br>Money grow and stay safe?</h2>
    <div class="abs brand brand-back"><span class="brand-mark"></span>The Wealth Compass</div>
    <div class="abs photo photo-back" role="img" aria-label="Photo of Daria Felt in a dark blazer, hand on hip"></div>
    <div class="abs work-box">
      <h3 class="work-title">Work with us to</h3>
      <ul class="work-list">
        <li>- Hire Daria as a Keynote Speaker</li>
        <li>- Teach Financial Literacy Workshops</li>
        <li>- Receive Financial Coaching</li>
      </ul>
    </div>
    <div class="abs learn-box">
      <p class="learn-q">Want To Learn More About How We Can Help?</p>
      <p class="learn-url">DariaFelt.com/Services</p>
    </div>
    <address class="abs contact">
      Daria Felt<br>Author | Speaker | Investor<br>daria@thewealthcompassbook.com<br><span class="tel">416-555-0187</span>
    </address>
    <div class="abs footer-band"></div>
  </section>
</body>
</html>
```